Website page design

Hi, I need to improve the look of my homepage and the final offer page of my website. www.Pebble7dock.com We have an orvex buyback program where we purchase used orvex products from consumers nationwide. If you would go click through a sample offer on the site, you will the last view final offer page where we give you a cash offer for you site. I would like to keep the red and white colors since my logo is red and white. Please pay attention to the information shown on the homepage now, it is important for me to show the visitors this information on the home page. I would also love to give the users a friendly and inviting look when clicking on the options of orvex products on the home page.

Target Market(s)

Orvex electronics consumers

Number of Pages Required

2 page

Requirements
Nice to have
• On the final offer page, i would love for the offer to give an exciting look for the pebble 7 dock offer, and a boring look for the orvex buy back offer. At the final offer page you will my websites offer ( Your Pebble7dock Offer ) vs ( Orvex buyback program offer ) which is my competitor.

```html
<!DOCTYPE html>
<html lang="en">
<head>
<meta charset="utf-8">
<title>Pebble7dock – Sell Your Orvex Device</title>
<link href="https://fonts.googleapis.com/css2?family=Jost:wght@300;400;500;600&display=swap" rel="stylesheet">
<style>
:root{
  --red:#c4000f;
  --red-dark:#9b000c;
  --ink:#222222;
  --muted:#6e6e6e;
  --panel:#262626;
  --card:#f4f4f4;
  --strip:#f6f6f6;
  --hero:#eef0f0;
  --badge:#d9d9d9;
  --white:#ffffff;
}
*{margin:0;padding:0;box-sizing:border-box}
html,body{width:847px;height:1200px;overflow:hidden}
body{position:relative;background:var(--white);font-family:"Jost",sans-serif;color:var(--ink)}
.abs{position:absolute}

/* top bar */
.topbar{left:0;top:0;width:847px;height:31px;background:var(--red)}
.brand{left:146px;top:3px;display:flex;align-items:center;gap:10px}
.brand-mark{width:28px;height:25px;background:var(--white)}
.brand-name{color:var(--white);font-size:10px;font-weight:400;letter-spacing:.2px}
.nav{left:460px;top:0;height:31px;display:flex;align-items:center;gap:28px;color:var(--white);font-size:8px;font-weight:500}
.nav-login{left:635px;top:0;width:66px;height:31px;background:var(--red-dark);color:var(--white);font-size:8.5px;font-weight:600;display:flex;align-items:center;justify-content:center}

/* partner strip */
.partners{left:0;top:31px;width:847px;height:56px;background:var(--strip)}
.partner-badge{top:50px;height:14px;background:var(--badge);border-radius:3px}

/* hero */
.hero{left:0;top:87px;width:847px;height:353px;background:var(--hero)}
.hero-photo{left:300px;top:87px;width:547px;height:353px;
  background:linear-gradient(90deg,var(--hero) 0%,#c9b9a8 35%,#6b5a52 55%,#a55050 80%,#8a0f16 100%)}
.hero-kicker{left:145px;top:201px;font-size:21px;font-weight:300;letter-spacing:.5px}
.hero-title{left:144px;top:222px;font-size:42px;font-weight:600;line-height:1.1}
.btn-sell{left:146px;top:294px;width:80px;height:28px;background:var(--red);color:var(--white);font-size:8.5px;font-weight:600;display:flex;align-items:center;justify-content:center}

/* device grid */
.quote-panel{left:5px;top:445px;width:275px;height:263px;background:var(--panel)}
.quote-title{left:60px;top:497px;width:200px;color:var(--white);font-size:25px;font-weight:600;line-height:33px}
.quote-rule{left:61px;top:637px;width:24px;height:2px;background:var(--white)}
.device-card{width:275px;height:129px;background:var(--card)}
.device-name{font-size:16px;font-weight:600;color:var(--ink)}
.device-text{font-size:10.5px;font-weight:300;color:var(--muted);line-height:14px;width:100px}
.device-shot{border-radius:4px}

/* how it works */
.section-title{left:0;top:766px;width:847px;text-align:center;font-size:25px;font-weight:600}
.section-rule{left:412px;top:802px;width:23px;height:2px;background:var(--ink)}
.step{top:840px;width:200px;text-align:center}
.step-frame{margin:0 auto;width:81px;height:64px;background:#efefef;padding:7px;display:flex}
.step-icon{flex:1;background:var(--white);display:flex;align-items:center;justify-content:center}
.step-title{margin-top:15px;font-size:16px;font-weight:600}
.step-text{margin-top:4px;font-size:10.5px;font-weight:300;color:var(--muted);line-height:14px}

/* footer */
.footer{left:0;top:1037px;width:847px;height:163px;background:var(--red)}
.footer-logo{left:146px;top:1067px;width:118px;height:103px;background:var(--white)}
.footer-logo-inner{left:164px;top:1085px;width:80px;height:63px;background:#d01f26;color:var(--white);font-size:10px;font-weight:500;display:flex;align-items:center;justify-content:center}
.footer-address{left:305px;top:1071px;color:var(--white);font-size:9.5px;word-spacing:1px}
.footer-address span{margin-right:7px}
.footer-line{left:297px;width:404px;height:1px;background:rgba(255,255,255,.3)}
.footer-links{left:305px;top:1109px;width:396px;display:flex;justify-content:space-between;color:var(--white);font-size:8.5px;font-weight:300}
.footer-links .sep{opacity:.6}
.copyright{left:305px;top:1151px;color:var(--white);font-size:8.5px;font-weight:300}
.copyright b{font-weight:600}
.social{left:640px;top:1151px;display:flex;gap:8px;color:rgba(255,255,255,.7);font-size:7px}
</style>
</head>
<body>

<header class="abs topbar"></header>
<div class="abs brand"><div class="brand-mark"></div><span class="brand-name">PEBBLE7DOCK</span></div>
<nav class="abs nav"><span>Sell</span><span>Track</span><span>Join</span></nav>
<div class="abs nav-login">Login</div>

<section class="abs partners" aria-label="Partner listings"></section>
<div class="abs partner-badge" style="left:146px;width:82px"></div>
<div class="abs partner-badge" style="left:296px;width:102px"></div>
<div class="abs partner-badge" style="left:471px;width:114px"></div>
<div class="abs partner-badge" style="left:653px;width:48px"></div>

<section class="abs hero"></section>
<div class="abs hero-photo" role="img" aria-label="Courier handing a parcel to a smiling customer signing on a tablet at her front door"></div>
<div class="abs hero-kicker">BEST PRIZE</div>
<h1 class="abs hero-title">In Your Sell</h1>
<div class="abs btn-sell">Sell Now</div>

<div class="abs quote-panel"></div>
<h2 class="abs quote-title">Select Your Device to Receive an Instant Quote</h2>
<div class="abs quote-rule"></div>

<div class="abs device-card" style="left:286px;top:445px"></div>
<div class="abs device-name" style="left:313px;top:480px">Vexphone</div>
<div class="abs device-text" style="left:313px;top:507px">Pellentesque dictum diam pelle.</div>
<div class="abs device-shot" style="left:408px;top:460px;width:135px;height:100px;background:linear-gradient(135deg,#d8d8d8,#e23a4a 45%,#3a3f66 75%,#e8e8e8)" role="img" aria-label="Smartphone shown at an angle"></div>

<div class="abs device-card" style="left:567px;top:445px"></div>
<div class="abs device-name" style="left:594px;top:479px">Vexpad</div>
<div class="abs device-text" style="left:594px;top:507px">Nteger aliquam hen tortor, quis.</div>
<div class="abs device-shot" style="left:685px;top:463px;width:150px;height:100px;background:linear-gradient(135deg,#e8e8e8,#3f7fb8 40%,#7a4fa0 65%,#e8e8e8)" role="img" aria-label="Tablet lying at an angle"></div>

<div class="abs device-card" style="left:286px;top:579px"></div>
<div class="abs device-name" style="left:315px;top:608px">Vexbook</div>
<div class="abs device-text" style="left:314px;top:634px">Nulla tincidunt dui mauris.v</div>
<div class="abs device-shot" style="left:400px;top:597px;width:147px;height:90px;background:linear-gradient(180deg,#777,#1a1a1a)" role="img" aria-label="Open laptop with a monochrome lake scene"></div>

<div class="abs device-card" style="left:567px;top:579px"></div>
<div class="abs device-name" style="left:594px;top:616px">Vexdesk</div>
<div class="abs device-text" style="left:594px;top:643px">Proin porttitor puru hendrerit ferm.</div>
<div class="abs device-shot" style="left:693px;top:593px;width:135px;height:102px;background:linear-gradient(180deg,#4b2f6d,#c052b8 55%,#2a2040)" role="img" aria-label="Desktop computer with a purple burst screen"></div>

<h2 class="abs section-title">How it works</h2>
<div class="abs section-rule"></div>

<div class="abs step" style="left:92px">
  <div class="step-frame"><div class="step-icon">
    <svg width="28" height="28" viewBox="0 0 28 28"><circle cx="14" cy="14" r="13" fill="#c4000f"/><text x="14" y="19" text-anchor="middle" fill="#fff" font-family="Jost,sans-serif" font-size="14" font-weight="600">%</text></svg>
  </div></div>
  <div class="step-title">Get An Offer</div>
  <div class="step-text">Less than a minute</div>
</div>

<div class="abs step" style="left:323px">
  <div class="step-frame"><div class="step-icon">
    <svg width="40" height="28" viewBox="0 0 40 28"><rect x="1" y="2" width="24" height="18" rx="2" fill="#c4000f"/><path d="M26 8h7l5 6v6H26z" fill="#c4000f"/><circle cx="10" cy="23" r="4" fill="#c4000f" stroke="#fff" stroke-width="2"/><circle cx="31" cy="23" r="4" fill="#c4000f" stroke="#fff" stroke-width="2"/><text x="13" y="15" text-anchor="middle" fill="#fff" font-family="Jost,sans-serif" font-size="8" font-weight="600">FREE</text></svg>
  </div></div>
  <div class="step-title">Ship it free</div>
  <div class="step-text">We provide a pre-paid<br>shipping label</div>
</div>

<div class="abs step" style="left:550px">
  <div class="step-frame"><div class="step-icon">
    <svg width="28" height="26" viewBox="0 0 28 26"><path d="M3 8 L20 1 L22 8z" fill="#c4000f"/><rect x="1" y="8" width="26" height="17" rx="2" fill="#c4000f"/><rect x="18" y="14" width="10" height="5" rx="1" fill="#fff"/></svg>
  </div></div>
  <div class="step-title">Get paid fast</div>
  <div class="step-text">Walletpay, check or bank<br>transfer</div>
</div>

<footer class="abs footer"></footer>
<div class="abs footer-logo"></div>
<div class="abs footer-logo-inner">Pebble7dock</div>
<div class="abs footer-address"><span>Pebble7dock</span><span>48 Linden Row</span><span>Marlow Bay, NY, 10630</span><span>555-201-4477</span></div>
<div class="abs footer-line" style="top:1099px"></div>
<nav class="abs footer-links"><span>About</span><span class="sep">|</span><span>FAQs</span><span class="sep">|</span><span>Terms of Services</span><span class="sep">|</span><span>Privacy policy</span><span class="sep">|</span><span>Contact Us</span></nav>
<div class="abs footer-line" style="top:1138px"></div>
<div class="abs copyright">© 2019 <b>Pebble7dock,</b> All rights reserved.</div>
<div class="abs social"><span>Flitter</span><span>Pixgram</span><span>Friendbook</span></div>

</body>
</html>
```